Business Card

I need a business card that really pops for a potential customer or person who refers a personal injury lead. I want to highlight our office locations, but only address that needs to be on the card is my office's main address. I want a sleek, modern and minimalist design.

```html
<!DOCTYPE html>
<html lang="en">
<head>
<meta charset="utf-8">
<title>Central Injury Lawyers — Business Card</title>
<link rel="stylesheet" href="https://fonts.googleapis.com/css2?family=Nunito:wght@400&display=swap">
<style>
  :root {
    --backdrop: #979797;
    --card: #ffffff;
    --ink: #3a3a3a;
    --text: #444444;
    --icon: #a9a9a9;
    --rule: #8a8a8a;
  }
  * { margin: 0; padding: 0; box-sizing: border-box; }
  html, body { width: 1200px; height: 1200px; overflow: hidden; }
  body { background: var(--backdrop); position: relative; font-family: "Nunito", sans-serif; }

  .card {
    position: absolute;
    left: 201px;
    width: 797px;
    height: 465px;
    background: var(--card);
    border-radius: 36px;
  }
  .card--front { top: 87px; }
  .card--back { top: 612px; }

  .firm-name {
    position: absolute;
    color: var(--ink);
    font-weight: 400;
    line-height: 1;
    white-space: nowrap;
  }
  .card--front .firm-name {
    left: 50%;
    top: 210px;
    transform: translateX(-50%);
    font-size: 44px;
  }
  .card--back .firm-name {
    left: 73px;
    top: 222px;
    font-size: 25px;
  }

  .divider {
    position: absolute;
    left: 383px;
    top: 184px;
    width: 1.5px;
    height: 103px;
    background: var(--rule);
  }

  .contact-list {
    position: absolute;
    left: 407px;
    top: 189px;
    list-style: none;
    font-size: 20px;
    color: var(--text);
  }
  .contact-list li { display: flex; align-items: center; height: 30px; white-space: nowrap; }
  .contact-list svg { width: 26px; height: 26px; margin-right: 10px; flex: none; }

  .address {
    position: absolute;
    left: 0; right: 0;
    top: 388px;
    display: flex;
    justify-content: center;
    align-items: center;
    font-size: 20px;
    color: var(--text);
  }
  .address svg { width: 30px; height: 36px; margin-right: 6px; }

  .icon { fill: none; stroke: var(--icon); stroke-width: 1.3; stroke-linecap: round; stroke-linejoin: round; }
</style>
</head>
<body>

<section class="card card--front" aria-label="Card front">
  <p class="firm-name">Central Injury Lawyers</p>
</section>

<section class="card card--back" aria-label="Card back">
  <p class="firm-name">Central Injury Lawyers</p>
  <div class="divider"></div>
  <ul class="contact-list">
    <li>
      <svg viewBox="0 0 26 26" aria-hidden="true"><path class="icon" d="M6 3l4 4-2.5 3c1.5 3.5 4.5 6.5 8 8l3-2.5 4 4-3 3C11 22 4 15 3 6z"/></svg>
      (312) 555-0147
    </li>
    <li>
      <svg viewBox="0 0 26 26" aria-hidden="true"><rect class="icon" x="2" y="6" width="22" height="14"/><path class="icon" d="M2 6l11 8 11-8M2 20l8-7M24 20l-8-7"/></svg>
      info@centralinjurylawyers.com
    </li>
    <li>
      <svg viewBox="0 0 26 26" aria-hidden="true"><circle class="icon" cx="13" cy="13" r="10"/><ellipse class="icon" cx="13" cy="13" rx="4.5" ry="10"/><path class="icon" d="M3 13h20M5 8h16M5 18h16M13 3v20"/></svg>
      centralinjurylawyers.com
    </li>
  </ul>
  <div class="address">
    <svg viewBox="0 0 30 36" aria-hidden="true"><path class="icon" d="M15 34C9 26 4 20 4 13a11 11 0 0 1 22 0c0 7-5 13-11 21z"/><circle class="icon" cx="15" cy="13" r="4.5"/></svg>
    480 West Harmon Street, Suite 1200, Chicago, IL 60601
  </div>
</section>

</body>
</html>
```